Business IT Services Billboard to attract local small businesses

We are Brivolux, a premier Managed Service Provider (MSP) specializing in comprehensive IT services and VOIP phone solutions exclusively for businesses. Our goal is to create a dynamic and visually engaging billboard advertisement that not only highlights our cutting-edge IT solutions but also emphasizes our state-of-the-art VOIP phone services. This billboard should communicate our commitment to providing innovative, reliable, and holistic technology solutions.
Target Market(s)
small business
Industry/Entity Type
Information Technology
Colors
Designer to choose colors to be used in the design.
Look and feel
Each slider illustrates characteristics of the customer's brand and the style your logo design should communicate.

```html
<!DOCTYPE html>
<html lang="en">
<head>
<meta charset="utf-8">
<title>Brivolux Billboard</title>
<link href="https://fonts.googleapis.com/css2?family=Poppins:wght@500;600;700;800&display=swap" rel="stylesheet">
<style>
  :root {
    --navy: #0d1b33;
    --blue: #1a73c0;
    --blue-light: #2a8ad8;
    --orange: #e8560c;
    --orange-light: #ff8a12;
    --white: #ffffff;
    --rule: #c9ced6;
    --stage: #d4d4d4;
    --device-dark: #2b3140;
    --device-mid: #4a5266;
    --screen-top: #f1ede8;
    --screen-bottom: #d9cdbf;
    --bezel: #33373d;
  }
  * { margin: 0; padding: 0; box-sizing: border-box; }
  html, body { width: 1185px; height: 1200px; overflow: hidden; }
  body {
    background: radial-gradient(ellipse at center, #e6e6e6 0%, var(--stage) 70%, #bdbdbd 100%);
    font-family: "Poppins", sans-serif;
    position: relative;
  }
  .billboard {
    position: absolute;
    left: 40px;
    top: 439px;
    width: 1105px;
    height: 322px;
    background: var(--white);
    overflow: hidden;
    box-shadow: 0 18px 30px rgba(0,0,0,0.18);
  }
  .billboard-shapes { position: absolute; inset: 0; }
  .tagline-tab {
    position: absolute; left: 42px; top: 27px;
    height: 28px; width: 340px;
    background: linear-gradient(90deg, var(--orange), var(--orange-light));
    clip-path: polygon(0 0, 94% 0, 100% 100%, 0 100%);
    color: var(--white); font-weight: 600; font-size: 19.5px;
    line-height: 28px; padding-left: 11px; white-space: nowrap;
  }
  .headline {
    position: absolute; left: 40px; top: 56px;
    font-weight: 800; font-size: 71px; line-height: 61px;
    letter-spacing: -1px; white-space: nowrap;
  }
  .headline-dark { color: var(--navy); display: block; }
  .headline-blue { color: var(--blue); display: block; }
  .subline {
    position: absolute; left: 40px; top: 190px;
    font-weight: 600; font-size: 14px; color: var(--navy); white-space: nowrap;
  }
  .call-tab {
    position: absolute; left: 0; top: 225px;
    width: 251px; height: 30px;
    background: linear-gradient(90deg, var(--orange), var(--orange-light));
    clip-path: polygon(0 0, 88% 0, 100% 100%, 0 100%);
    color: var(--white); font-weight: 600; font-size: 20px;
    line-height: 30px; padding-left: 41px; white-space: nowrap;
  }
  .phone-line {
    position: absolute; left: 40px; top: 258px;
    display: flex; align-items: center; gap: 8px;
    color: var(--white); font-weight: 700; font-size: 52px; line-height: 64px;
    white-space: nowrap;
  }
  .phone-line svg { width: 34px; height: 34px; flex: none; }
  .brand-name {
    position: absolute; right: 54px; top: 14px;
    color: var(--white); font-weight: 700; font-size: 36px;
    letter-spacing: 6px; text-transform: uppercase; white-space: nowrap;
  }
  .desk-phone-photo {
    position: absolute; left: 560px; top: 118px; width: 162px; height: 126px;
    border-radius: 18px 18px 12px 12px;
    background: linear-gradient(160deg, var(--device-mid) 0%, var(--device-dark) 70%);
    box-shadow: 0 8px 14px rgba(0,0,0,0.18);
  }
  .laptop-photo {
    position: absolute; left: 736px; top: 64px; width: 338px; height: 192px;
    border-radius: 8px;
    border: 7px solid var(--bezel);
    border-bottom-width: 12px;
    background: linear-gradient(180deg, var(--screen-top) 0%, var(--screen-bottom) 100%);
    box-shadow: 0 8px 14px rgba(0,0,0,0.18);
  }
  .visit-label {
    position: absolute; left: 562px; top: 279px;
    font-weight: 600; font-size: 14px; color: var(--navy); white-space: nowrap;
  }
  .url-pill {
    position: absolute; left: 794px; top: 270px;
    width: 256px; height: 30px; border-radius: 15px;
    background: linear-gradient(90deg, var(--orange), var(--orange-light));
    color: var(--white); font-weight: 700; font-size: 21px;
    line-height: 30px; text-align: center; white-space: nowrap;
  }
</style>
</head>
<body>
  <section class="billboard">
    <svg class="billboard-shapes" viewBox="0 0 1105 322" preserveAspectRatio="none">
      <defs>
        <linearGradient id="skyBlue" x1="0" y1="0" x2="1" y2="1">
          <stop offset="0" stop-color="#2a8ad8"/>
          <stop offset="1" stop-color="#1565b0"/>
        </linearGradient>
      </defs>
      <polygon points="512,0 1105,0 1105,140 722,146" fill="url(#skyBlue)"/>
      <line x1="495" y1="0" x2="712" y2="150" stroke="var(--rule)" stroke-width="3"/>
      <line x1="722" y1="150" x2="1105" y2="144" stroke="var(--rule)" stroke-width="2"/>
      <polygon points="0,255 481,255 567,322 0,322" fill="var(--blue)"/>
      <rect x="567" y="316" width="538" height="6" fill="var(--blue)"/>
    </svg>

    <div class="tagline-tab">ELEVATE YOUR BUSINESS WITH</div>
    <h1 class="headline">
      <span class="headline-dark">Next-Gen IT</span>
      <span class="headline-blue">and Phones</span>
    </h1>
    <p class="subline">Innovative IT and VOIP Solutions Tailored for Your Business Success.</p>

    <div class="call-tab">CALL US TODAY</div>
    <div class="phone-line">
      <svg viewBox="0 0 24 24" fill="none" stroke="currentColor" stroke-width="2" stroke-linecap="round" stroke-linejoin="round">
        <path d="M22 16.9v3a2 2 0 0 1-2.2 2 19.8 19.8 0 0 1-8.6-3.1 19.5 19.5 0 0 1-6-6A19.8 19.8 0 0 1 2.1 4.2 2 2 0 0 1 4.1 2h3a2 2 0 0 1 2 1.7c.1 1 .4 1.9.7 2.8a2 2 0 0 1-.5 2.1L8 9.9a16 16 0 0 0 6 6l1.3-1.3a2 2 0 0 1 2.1-.4c.9.3 1.8.6 2.8.7a2 2 0 0 1 1.7 2z"/>
        <path d="M15 3a6 6 0 0 1 6 6M15 7a2 2 0 0 1 2 2"/>
      </svg>
      <span>(555) 014-2278</span>
    </div>

    <div class="brand-name">Brivolux</div>

    <div class="desk-phone-photo" role="img" aria-label="Black VOIP desk phone"></div>
    <div class="laptop-photo" role="img" aria-label="Laptop showing the company website homepage"></div>

    <p class="visit-label">Transform Your Tech Today at</p>
    <div class="url-pill">www.brivolux.com</div>
  </section>
</body>
</html>
```